FinTech Website + Mobile Design.

We require an new fresh Professional looking upgrade for our company website.

We are Australia's first professional crowd funding platform. Currently listed on the QTB(Harbour Share Bourse) and soon to be listed on the PLM(Continental Equity Bourse)

We are looking for a clean simple but professional look with clear focus the two main objectives "Investing" and "Borrowing"

Vantoro is a professional crowdfunding platform focused at servicing SME’s and non-sophisticated Investors.
Our platform lets borrowers access funds of $100,000 to $5 Million form our user base of over 50,000 members. Borrowers choose the rate they are prepared offer Investors and Investors select the opportunities they would like to invest in with average returns of 12%pa*.

Our platform gives Investors and borrows a real alternative to conventional banking. Funding can be done in as little as 45days*.

We need the design to be responsive.

The are some Charts and Statistics that will need graphics producing.

We will require Photoshop files, fonts and assets only. Not HTML or CSS.

Reference sites
https://pellivox.com
https://www.drumbelow.com
https://www.tarnifell.com
https://au.quillsporttrades.com/
Updates

This project has been extended by 5 Days. I look forward to see your designs. Cheers Dorian

Dear Designers, Please don't forget to include a Mobile version of your designs. Thanks Dorian

Hi All Designers, I will be closing this project in two days. Don't miss out. Get your designs in as soon as you can. Cheers Dorian

Target Market(s)

Investors, Dwell Weekly developers, Small business' Medium business.

Industry/Entity Type

Finance

Number of Pages Required

1 page

Font styles to use
Sans Serif

Requirements
Must have
• Clean Professional design
• Bright and fresh look
• Mobile design/responsive
Nice to have
• Animations

```html
<!DOCTYPE html>
<html lang="en">
<head>
<meta charset="utf-8">
<title>Vantoro – Crowdfunding for Investors and Borrowers</title>
<link rel="stylesheet" href="https://fonts.googleapis.com/css2?family=Open+Sans:wght@300;400;600;700&display=swap">
<style>
:root{
  --yellow:#f5c400;
  --red:#e02f2f;
  --green:#2f9e3f;
  --blue:#2b7fd6;
  --teal:#1fb3c9;
  --orange:#f39a1e;
  --ink:#333;
  --heading:#222;
  --line:#e2e2e2;
  --pale:#f1f1f1;
}
*{box-sizing:border-box;margin:0;padding:0}
html,body{width:1200px;height:3529px;overflow:hidden}
body{position:relative;background:#fff;font-family:'Open Sans',Arial,sans-serif;color:var(--ink)}
section,header,footer{position:absolute;left:0;width:1200px}
.abs{position:absolute}

/* brand name: plain text only */
.brand{position:absolute;font-weight:700;color:var(--heading);font-size:22px;line-height:26px}

/* header */
.site-header{top:0;height:94px;background:#fff;border-bottom:1px solid var(--line)}
.site-header .brand{left:90px;top:33px}
.ticker{position:absolute;left:265px;top:36px;font-size:14px;font-weight:600;color:#222}
.ticker b{color:var(--green);margin-right:4px}
.main-nav{position:absolute;right:90px;top:26px;display:flex;align-items:center;gap:36px;font-size:14px}
.main-nav a{color:#333;text-decoration:none}
.main-nav .current{color:var(--red)}
.main-nav .join{background:var(--yellow);color:#222;padding:12px 16px;font-weight:600}

/* hero */
.hero{top:94px;height:490px;background:linear-gradient(180deg,#07122e 0%,#132a66 45%,#1b3c7f 70%,#0a1430 100%)}
.hero-visual{position:absolute;left:0;top:230px;width:1200px;height:260px;background:linear-gradient(180deg,rgba(40,80,160,0) 0%,rgba(90,120,180,.45) 40%,rgba(30,40,70,.9) 100%)}
.hero-copy{position:absolute;top:140px;width:100%;text-align:center;color:#fff;font-size:16px;line-height:22px}
.hero-copy em{font-style:normal;color:var(--yellow);font-weight:600}
.hero-cta{position:absolute;top:200px;width:238px;height:56px;border:2px solid #fff;color:#fff;font-size:24px;font-weight:600;text-align:center;line-height:52px}
.hero-cta span{position:absolute;left:50%;transform:translateX(-50%);top:56px;width:118px;height:18px;font-size:10px;line-height:18px;font-weight:400}
.hero-cta.invest{left:360px}.hero-cta.invest span{background:var(--yellow);color:#222}
.hero-cta.found{left:607px}.hero-cta.found span{background:var(--red);color:#fff}

/* press band */
.press-band{top:584px;height:86px;background:linear-gradient(#eaeaea,#d4d4d4);display:flex;align-items:center;justify-content:space-around;padding:0 70px}
.press-name{font-size:13px;font-weight:700;color:#333;white-space:nowrap}

/* projects */
.projects{top:670px;height:530px;background:#fff}
.slider-arrow{position:absolute;top:200px;color:#888;font-size:30px}
.card{position:absolute;top:36px;width:236px;height:454px;border:1px solid var(--line);background:#fff}
.card-photo{height:146px;background:linear-gradient(135deg,#b3262a,#5a1013)}
.card-tag{position:absolute;left:0;top:0;width:100%;height:28px;background:rgba(0,0,0,.55);color:#fff;font-size:12px;font-weight:700;line-height:28px;padding-left:8px}
.card-body{padding:8px 10px}
.raised{display:flex;justify-content:space-between;font-size:14px;color:var(--green);font-weight:600}
.raised small{color:#333;font-size:9px;font-weight:400}
.bar{display:flex;align-items:center;gap:8px;margin:10px 0 12px}
.bar .track{flex:1;height:5px;background:#ddd}
.bar .track i{display:block;width:70%;height:5px;background:var(--blue)}
.card-blurb{font-size:11.5px;line-height:15px;border-bottom:1px solid var(--line);padding-bottom:12px}
.facts{display:grid;grid-template-columns:1fr 1fr;gap:9px 6px;font-size:10px;padding:12px 0;border-bottom:1px solid var(--line)}
.facts span{display:flex;align-items:center;gap:5px}
.facts svg{flex:none}
.fund-btn{display:block;margin-top:12px;border:2px solid var(--green);text-align:center;font-size:11.5px;font-weight:700;height:36px;line-height:32px}

/* insight */
.insight{top:1200px;height:435px;background:var(--pale)}
.insight h2{position:absolute;left:86px;top:56px;width:430px;font-weight:300;font-size:30px;line-height:36px;color:#222}
.insight p{position:absolute;left:86px;width:410px;font-size:11px;line-height:20px;color:#444}
.insight .lead{top:180px}
.insight .note{top:330px;font-weight:700;color:#222;line-height:17px}
.legend{position:absolute;top:66px;display:flex;align-items:flex-end;gap:6px}
.pill{color:#fff;font-size:11px;font-weight:700;padding:4px 10px}
.growth{background:#fff;padding:4px 10px 2px;font-size:11px;text-align:center;line-height:14px}
.growth b{display:block;font-size:24px;font-weight:300;color:var(--orange);line-height:26px}
.chart-map{position:absolute;left:560px;top:150px;width:470px;height:190px;background:radial-gradient(ellipse at center,#dcdcdc 0%,rgba(220,220,220,0) 70%)}
.chart-caption{position:absolute;left:530px;top:360px;width:460px;height:20px;background:#9a9a9a;color:#fff;font-size:8.5px;text-align:center;line-height:20px}

/* stats */
.stats{top:1635px;height:360px;background:linear-gradient(160deg,#2a2a2a 0%,#4a4d52 40%,#1e2024 100%)}
.stat{position:absolute;top:100px;width:160px;height:160px}
.stat b{position:absolute;inset:0;display:flex;align-items:center;justify-content:center;color:#fff;font-size:34px;font-weight:300}
.stat b small{font-size:14px;margin-top:14px}

/* ipo */
.ipo{top:1995px;height:518px;background:#fff}
.ipo-photo{position:absolute;left:160px;top:64px;width:353px;height:393px;background:linear-gradient(160deg,#5d86b5 0%,#9bb7d4 40%,#3e5a80 100%)}
.ipo h3{position:absolute;left:548px;top:64px;font-size:32px;font-weight:300}
.ipo .status{position:absolute;left:895px;top:78px;font-size:12px;font-weight:600}
.ipo .issuer{position:absolute;left:548px;top:104px;width:490px;border-bottom:1px solid var(--line);padding-bottom:6px;color:var(--blue);font-size:13px;font-weight:700}
.ipo .issuer small{font-weight:400;font-size:11px}
.ipo-grid{position:absolute;left:548px;top:136px;display:grid;grid-template-columns:155px 155px;gap:6px}
.ipo-cell{height:64px;background:var(--pale);display:flex;flex-direction:column;align-items:center;justify-content:center;font-size:16px;position:relative}
.ipo-cell small{position:absolute;right:6px;bottom:4px;font-size:8px;color:#999}
.ipo-cell.c1{border-top:3px solid var(--orange)}.ipo-cell.c2{border-left:3px solid var(--red)}
.ipo-cell.c3{border-left:3px solid var(--blue)}.ipo-cell.c4{border-top:3px solid #bbb}
.ipo .brand{left:916px;top:188px;font-size:16px;line-height:20px}
.ipo p{position:absolute;left:548px;top:290px;width:490px;font-size:12.5px;line-height:21px;color:#444}
.ipo-btn{position:absolute;top:402px;width:190px;height:54px;border:2px solid #333;text-align:center;line-height:50px;font-size:15px;font-weight:600}
.ipo-arrow{position:absolute;top:250px;width:24px;height:24px;background:#ccc;color:#fff;text-align:center;line-height:24px;font-size:12px}

/* press grid */
.press-grid{top:2513px;height:327px;background:#fff;border-top:1px solid var(--line);display:grid;grid-template-columns:repeat(7,1fr);align-items:center;justify-items:center;padding:28px 110px}
.press-grid .press-name{font-size:14px;color:#444}

/* crowdfunders */
.team{top:2840px;height:395px;background:linear-gradient(180deg,#151515 0%,#2f2a26 60%,#3a2b1e 100%)}
.team h2{position:absolute;top:62px;width:100%;text-align:center;color:#fff;font-size:19px;font-weight:700}
.member{position:absolute;top:110px;width:200px;text-align:center;color:#fff}
.member .portrait{width:156px;height:156px;margin:0 auto;border-radius:50%;border:5px solid #fff;background:linear-gradient(#e8e3dc,#bfb5a8)}
.member b{display:block;margin-top:14px;font-size:14px;font-weight:600}
.member span{display:block;font-size:11px;color:#ccc}
.team .arrow{position:absolute;top:180px;color:#888;font-size:20px}

/* footer */
.footer-nav{top:3235px;height:59px;background:#eee;display:flex;justify-content:center;align-items:center;gap:60px;font-size:12px;color:#555}
.footer-legal{top:3294px;height:188px;background:#eee;border-top:1px solid #ddd}
.partners{position:absolute;left:94px;top:26px;display:flex;flex-direction:column;gap:20px}
.partners .press-name{color:#333;font-size:15px}
.legal-text{position:absolute;left:272px;top:26px;width:690px;font-size:7.5px;line-height:10.5px;color:#555}
.badge{position:absolute;left:1040px;width:66px;height:30px;background:#d7d7d7}
.footer-bottom{top:3482px;height:47px;background:#262626}
.footer-bottom .brand{left:90px;top:13px;font-size:16px;line-height:20px;color:#fff}
.copyright{position:absolute;right:90px;top:18px;color:#888;font-size:9px}
</style>
</head>
<body>

<header class="site-header">
  <div class="brand">Vantoro</div>
  <div class="ticker"><b>▲</b>2.3%</div>
  <nav class="main-nav">
    <a class="current">Home</a><a>Invest</a><a>Get Found</a><a>About Us</a>
    <a class="join">Join</a><a>⇥ Sign in</a>
  </nav>
</header>

<section class="hero">
  <div class="hero-visual" role="img" aria-label="Night skyline of a harbour city with lit towers reflected in the water"></div>
  <div class="hero-copy">Lorem ipsum dolor sit amet, consect<br><em>etuer adipiscing elit.</em></div>
  <div class="hero-cta invest">Invest<span>Learn More</span></div>
  <div class="hero-cta found">Get Found<span>Learn More</span></div>
</section>

<section class="press-band">
  <span class="press-name">Norvale</span><span class="press-name">Brightwire</span><span class="press-name">Harbour Times</span>
  <span class="press-name">Techmeridian</span><span class="press-name">The Trade Ledger</span><span class="press-name">Kestrel News</span>
  <span class="press-name">The Coastal Herald</span><span class="press-name">Orbit Daily</span><span class="press-name">Qelna</span>
  <span class="press-name">Daily Courier</span>
</section>

<section class="projects">
  <div class="slider-arrow" style="left:36px">‹</div>
  <div class="slider-arrow" style="right:36px">›</div>

  <article class="card" style="left:89px">
    <div class="card-photo" role="img" aria-label="Hand holding a red drink can"></div>
    <div class="card-tag">Regeon!</div>
    <div class="card-body">
      <div class="raised">Aus $3,821,067 <small>98%</small></div>
      <div class="bar"><svg width="16" height="12"><path d="M1 1l14 5-14 5 4-5z" fill="none" stroke="#999"/></svg><span class="track"><i></i></span></div>
      <p class="card-blurb">Merchandisign made easy for the Creators of this World!</p>
      <div class="facts">
        <span><svg width="10" height="10"><rect x="1" y="4" width="2" height="6" fill="#2b7fd6"/><rect x="4" y="2" width="2" height="8" fill="#2b7fd6"/><rect x="7" y="0" width="2" height="10" fill="#2b7fd6"/></svg>12% PA</span>
        <span><svg width="10" height="10"><rect x="0" y="1" width="10" height="9" fill="none" stroke="#2b7fd6"/><line x1="0" y1="4" x2="10" y2="4" stroke="#2b7fd6"/></svg>12 Months</span>
        <span><svg width="10" height="10"><rect x="0" y="2" width="10" height="7" fill="none" stroke="#2b7fd6"/></svg>AU$2,500,000</span>
        <span><svg width="10" height="10"><path d="M5 10C1 5 1 4 1 4a4 4 0 018 0s0 1-4 6z" fill="#2b7fd6"/></svg>Perth, Australia</span>
        <span><svg width="10" height="10"><path d="M5 0v7M2 4l3 3 3-3M0 9h10" stroke="#2b7fd6" fill="none"/></svg>AU$50,000 min</span>
        <span><svg width="10" height="10"><circle cx="5" cy="3" r="2.5" fill="#2b7fd6"/><path d="M1 10a4 4 0 018 0z" fill="#2b7fd6"/></svg>100</span>
        <span><svg width="10" height="10"><circle cx="5" cy="5" r="4" fill="none" stroke="#2b7fd6"/><path d="M5 2v3h2" stroke="#2b7fd6" fill="none"/></svg>27 Days Left</span>
        <span><svg width="10" height="10"><circle cx="5" cy="3" r="2.5" fill="#2b7fd6"/><path d="M1 10a4 4 0 018 0z" fill="#2b7fd6"/></svg>22 Investors</span>
      </div>
      <span class="fund-btn">Fund this Project</span>
    </div>
  </article>

  <article class="card" style="left:350px">
    <div class="card-photo" style="background:linear-gradient(135deg,#c0392b,#3a0d0d)" role="img" aria-label="Woman with a bottle against a red backdrop"></div>
    <div class="card-tag">Regeon!</div>
    <div class="card-body">
      <div class="raised">Aus $3,821,067 <small>98%</small></div>
      <div class="bar"><svg width="16" height="12"><path d="M1 1l14 5-14 5 4-5z" fill="none" stroke="#999"/></svg><span class="track"><i></i></span></div>
      <p class="card-blurb">Merchandisign made easy for the Creators of this World!</p>
      <div class="facts">
        <span><svg width="10" height="10"><rect x="1" y="4" width="2" height="6" fill="#2b7fd6"/><rect x="4" y="2" width="2" height="8" fill="#2b7fd6"/><rect x="7" y="0" width="2" height="10" fill="#2b7fd6"/></svg>12% PA</span>
        <span><svg width="10" height="10"><rect x="0" y="1" width="10" height="9" fill="none" stroke="#2b7fd6"/><line x1="0" y1="4" x2="10" y2="4" stroke="#2b7fd6"/></svg>12 Months</span>
        <span><svg width="10" height="10"><rect x="0" y="2" width="10" height="7" fill="none" stroke="#2b7fd6"/></svg>AU$2,500,000</span>
        <span><svg width="10" height="10"><path d="M5 10C1 5 1 4 1 4a4 4 0 018 0s0 1-4 6z" fill="#2b7fd6"/></svg>Perth, Australia</span>
        <span><svg width="10" height="10"><path d="M5 0v7M2 4l3 3 3-3M0 9h10" stroke="#2b7fd6" fill="none"/></svg>AU$50,000 min</span>
        <span><svg width="10" height="10"><circle cx="5" cy="3" r="2.5" fill="#2b7fd6"/><path d="M1 10a4 4 0 018 0z" fill="#2b7fd6"/></svg>100</span>
        <span><svg width="10" height="10"><circle cx="5" cy="5" r="4" fill="none" stroke="#2b7fd6"/><path d="M5 2v3h2" stroke="#2b7fd6" fill="none"/></svg>27 Days Left</span>
        <span><svg width="10" height="10"><circle cx="5" cy="3" r="2.5" fill="#2b7fd6"/><path d="M1 10a4 4 0 018 0z" fill="#2b7fd6"/></svg>22 Investors</span>
      </div>
      <span class="fund-btn">Fund this Project</span>
    </div>
  </article>

  <article class="card" style="left:611px">
    <div class="card-photo" style="background:linear-gradient(135deg,#8a8f98,#3b3f46)" role="img" aria-label="Person surrounded by a wall of screens"></div>
    <div class="card-tag">Regeon!</div>
    <div class="card-body">
      <div class="raised">Aus $3,821,067 <small>98%</small></div>
      <div class="bar"><svg width="16" height="12"><path d="M1 1l14 5-14 5 4-5z" fill="none" stroke="#999"/></svg><span class="track"><i></i></span></div>
      <p class="card-blurb">Merchandisign made easy for the Creators of this World!</p>
      <div class="facts">
        <span><svg width="10" height="10"><rect x="1" y="4" width="2" height="6" fill="#2b7fd6"/><rect x="4" y="2" width="2" height="8" fill="#2b7fd6"/><rect x="7" y="0" width="2" height="10" fill="#2b7fd6"/></svg>12% PA</span>
        <span><svg width="10" height="10"><rect x="0" y="1" width="10" height="9" fill="none" stroke="#2b7fd6"/><line x1="0" y1="4" x2="10" y2="4" stroke="#2b7fd6"/></svg>12 Months</span>
        <span><svg width="10" height="10"><rect x="0" y="2" width="10" height="7" fill="none" stroke="#2b7fd6"/></svg>AU$2,500,000</span>
        <span><svg width="10" height="10"><path d="M5 10C1 5 1 4 1 4a4 4 0 018 0s0 1-4 6z" fill="#2b7fd6"/></svg>Perth, Australia</span>
        <span><svg width="10" height="10"><path d="M5 0v7M2 4l3 3 3-3M0 9h10" stroke="#2b7fd6" fill="none"/></svg>AU$50,000 min</span>
        <span><svg width="10" height="10"><circle cx="5" cy="3" r="2.5" fill="#2b7fd6"/><path d="M1 10a4 4 0 018 0z" fill="#2b7fd6"/></svg>100</span>
        <span><svg width="10" height="10"><circle cx="5" cy="5" r="4" fill="none" stroke="#2b7fd6"/><path d="M5 2v3h2" stroke="#2b7fd6" fill="none"/></svg>27 Days Left</span>
        <span><svg width="10" height="10"><circle cx="5" cy="3" r="2.5" fill="#2b7fd6"/><path d="M1 10a4 4 0 018 0z" fill="#2b7fd6"/></svg>22 Investors</span>
      </div>
      <span class="fund-btn">Fund this Project</span>
    </div>
  </article>

  <article class="card" style="left:872px">
    <div class="card-photo" style="background:linear-gradient(135deg,#6b1818,#1c1010)" role="img" aria-label="Two people in costume against a dark red backdrop"></div>
    <div class="card-tag">Regeon!</div>
    <div class="card-body">
      <div class="raised">Aus $3,821,067 <small>98%</small></div>
      <div class="bar"><svg width="16" height="12"><path d="M1 1l14 5-14 5 4-5z" fill="none" stroke="#999"/></svg><span class="track"><i></i></span></div>
      <p class="card-blurb">Merchandisign made easy for the Creators of this World!</p>
      <div class="facts">
        <span><svg width="10" height="10"><rect x="1" y="4" width="2" height="6" fill="#2b7fd6"/><rect x="4" y="2" width="2" height="8" fill="#2b7fd6"/><rect x="7" y="0" width="2" height="10" fill="#2b7fd6"/></svg>12% PA</span>
        <span><svg width="10" height="10"><rect x="0" y="1" width="10" height="9" fill="none" stroke="#2b7fd6"/><line x1="0" y1="4" x2="10" y2="4" stroke="#2b7fd6"/></svg>12 Months</span>
        <span><svg width="10" height="10"><rect x="0" y="2" width="10" height="7" fill="none" stroke="#2b7fd6"/></svg>AU$2,500,000</span>
        <span><svg width="10" height="10"><path d="M5 10C1 5 1 4 1 4a4 4 0 018 0s0 1-4 6z" fill="#2b7fd6"/></svg>Perth, Australia</span>
        <span><svg width="10" height="10"><path d="M5 0v7M2 4l3 3 3-3M0 9h10" stroke="#2b7fd6" fill="none"/></svg>AU$50,000 min</span>
        <span><svg width="10" height="10"><circle cx="5" cy="3" r="2.5" fill="#2b7fd6"/><path d="M1 10a4 4 0 018 0z" fill="#2b7fd6"/></svg>100</span>
        <span><svg width="10" height="10"><circle cx="5" cy="5" r="4" fill="none" stroke="#2b7fd6"/><path d="M5 2v3h2" stroke="#2b7fd6" fill="none"/></svg>27 Days Left</span>
        <span><svg width="10" height="10"><circle cx="5" cy="3" r="2.5" fill="#2b7fd6"/><path d="M1 10a4 4 0 018 0z" fill="#2b7fd6"/></svg>22 Investors</span>
      </div>
      <span class="fund-btn">Fund this Project</span>
    </div>
  </article>
</section>

<section class="insight">
  <h2>Did you know? Investors who diversify into real estate outperform those who don’t.</h2>
  <p class="lead">Historically, investors with roughly 20% allocated to real estate have outperformed those who only own stocks and bonds. However, the best opportunities require minimums of $100,000 or more, making them inaccessible unless you’re very wealthy. The only other option is to go through unnecessary middlemen who charge high fees, negatively impacting returns.</p>
  <p class="note">An investment in the common shares of any of the electronic real estate investment trusts (the eREITs) involves substantial risks. Each investor shoul</p>

  <div class="legend" style="left:600px">
    <span class="pill" style="background:var(--teal)">Real Estate</span>
    <span class="growth"><b>482%</b>Growth</span>
    <span class="growth"><b>80%</b>Growth</span>
    <span class="pill" style="background:var(--teal)">Equity 500</span>
  </div>
  <div class="chart-map" role="img" aria-label="Faint world map behind the chart"></div>
  <svg class="abs" style="left:530px;top:120px" width="470" height="240" viewBox="0 0 470 240">
    <g fill="#8a8a8a"><circle cx="32" cy="16" r="13"/><circle cx="80" cy="16" r="13"/><circle cx="128" cy="16" r="13"/><circle cx="176" cy="16" r="13"/><circle cx="224" cy="16" r="13"/><circle cx="272" cy="16" r="13"/><circle cx="320" cy="16" r="13"/><circle cx="368" cy="16" r="13"/><circle cx="416" cy="16" r="13"/></g>
    <g fill="#fff" font-size="8" text-anchor="middle" font-family="Open Sans, sans-serif"><text x="32" y="19">2000</text><text x="80" y="19">2002</text><text x="128" y="19">2004</text><text x="176" y="19">2006</text><text x="224" y="19">2008</text><text x="272" y="19">2010</text><text x="320" y="19">2012</text><text x="368" y="19">2014</text><text x="416" y="19">2016</text></g>
    <g stroke="#bbb" stroke-dasharray="2 3"><line x1="32" y1="30" x2="32" y2="230"/><line x1="80" y1="30" x2="80" y2="230"/><line x1="128" y1="30" x2="128" y2="230"/><line x1="176" y1="30" x2="176" y2="230"/><line x1="224" y1="30" x2="224" y2="230"/><line x1="272" y1="30" x2="272" y2="230"/><line x1="320" y1="30" x2="320" y2="230"/><line x1="368" y1="30" x2="368" y2="230"/><line x1="416" y1="30" x2="416" y2="230"/></g>
    <g>
      <rect x="18" y="210" width="10" height="20" fill="#1fb3c9"/><rect x="32" y="215" width="10" height="15" fill="#f39a1e"/>
      <rect x="66" y="195" width="10" height="35" fill="#f39a1e"/><rect x="80" y="190" width="10" height="40" fill="#1fb3c9"/>
      <rect x="114" y="175" width="10" height="55" fill="#1fb3c9"/><rect x="128" y="180" width="10" height="50" fill="#e02f2f"/>
      <rect x="162" y="170" width="10" height="60" fill="#e02f2f"/><rect x="176" y="160" width="10" height="70" fill="#1fb3c9"/>
      <rect x="210" y="150" width="10" height="80" fill="#1fb3c9"/><rect x="224" y="140" width="10" height="90" fill="#e02f2f"/>
      <rect x="258" y="130" width="10" height="100" fill="#e02f2f"/><rect x="272" y="135" width="10" height="95" fill="#1fb3c9"/>
      <rect x="306" y="110" width="10" height="120" fill="#1fb3c9"/><rect x="320" y="95" width="10" height="135" fill="#e02f2f"/>
      <rect x="354" y="80" width="10" height="150" fill="#e02f2f"/><rect x="368" y="70" width="10" height="160" fill="#1fb3c9"/>
      <rect x="402" y="60" width="10" height="170" fill="#f39a1e"/><rect x="416" y="50" width="10" height="180" fill="#f39a1e"/>
    </g>
  </svg>
  <div class="chart-caption">Global REIT Index vs. Equity 500, Growth in percentage, Jan 1, 2000–Dec 31, 2015 (dividends reinvested)</div>
</section>

<section class="stats" role="region" aria-label="Key figures">
  <div class="stat" style="left:155px"><svg width="160" height="160"><circle cx="80" cy="80" r="76" fill="none" stroke="rgba(255,255,255,.6)" stroke-width="1.5"/><path d="M80 4A76 76 0 0 1 152 58" fill="none" stroke="#1fb3c9" stroke-width="7"/></svg><b>423<small>%</small></b></div>
  <div class="stat" style="left:402px"><svg width="160" height="160"><circle cx="80" cy="80" r="76" fill="none" stroke="rgba(255,255,255,.6)" stroke-width="1.5"/><path d="M80 4A76 76 0 0 1 140 126" fill="none" stroke="#f39a1e" stroke-width="7"/></svg><b>45<small>m</small></b></div>
  <div class="stat" style="left:645px"><svg width="160" height="160"><circle cx="80" cy="80" r="76" fill="none" stroke="rgba(255,255,255,.6)" stroke-width="1.5"/><path d="M80 4A76 76 0 0 1 80 156" fill="none" stroke="#e02f2f" stroke-width="7"/></svg><b>50<small>k</small></b></div>
  <div class="stat" style="left:890px"><svg width="160" height="160"><circle cx="80" cy="80" r="76" fill="none" stroke="rgba(255,255,255,.6)" stroke-width="1.5"/><path d="M80 4A76 76 0 0 1 130 23" fill="none" stroke="#1fb3c9" stroke-width="7"/></svg><b>14<small>%</small></b></div>
</section>

<section class="ipo">
  <div class="ipo-arrow" style="left:89px">◀</div>
  <div class="ipo-arrow" style="left:1087px">▶</div>
  <div class="ipo-photo" role="img" aria-label="Glass office towers seen from below against a blue sky"></div>
  <h3>IPO</h3>
  <div class="status">Quillsport Biding Closed</div>
  <div class="issuer">Vantoro Limited <small>PLM:VTR</small></div>
  <div class="ipo-grid">
    <div class="ipo-cell c1">$0.40<small>Price</small></div>
    <div class="ipo-cell c2">$5 - $10<small>Range</small></div>
    <div class="ipo-cell c3">24 May 16<small>Open</small></div>
    <div class="ipo-cell c4">30 Jun 16<small>Close</small></div>
  </div>
  <div class="brand">Vantoro</div>
  <p>Vantoro Limited (PLM:VTR) is a web-based real estate and business crowdfunding platform that connects investors with businesses that need capital. Established in 2013, it operates across Asia with offices in Singapore, Australia, China, Malaysia and Indonesia and has successfully funded 67 real estate and SME projects.</p>
  <div class="ipo-btn" style="left:548px">Read More</div>
  <div class="ipo-btn" style="left:750px;border-color:var(--blue)">Bid</div>
</section>

<section class="press-grid">
  <span class="press-name">Norvale</span><span class="press-name">Brightwire</span><span class="press-name">Harbour Times</span><span class="press-name">Techmeridian</span><span class="press-name">The Trade Ledger</span><span class="press-name">Kestrel News</span><span class="press-name">The Coastal Herald</span>
  <span class="press-name">Capital Review</span><span class="press-name">Orbit Daily</span><span class="press-name">Qelna</span><span class="press-name">Daily Courier</span><span class="press-name">Pledge Insider</span><span class="press-name">Ferndale Media</span><span class="press-name">The Epoch</span>
  <span class="press-name">Dwell Weekly</span><span class="press-name">The Southlander</span><span class="press-name">Ridge Property</span><span class="press-name">Wealth Forum</span><span class="press-name">Centrix</span><span class="press-name">Jorra</span><span class="press-name">Suara Pelangi</span>
</section>

<section class="team">
  <h2>Crowdfunders</h2>
  <span class="arrow" style="left:88px">‹</span><span class="arrow" style="right:88px">›</span>
  <div class="member" style="left:243px"><div class="portrait" role="img" aria-label="Portrait of Jonny George"></div><b>Jonny George</b><span>Annalizer</span><span>...</span></div>
  <div class="member" style="left:495px"><div class="portrait" role="img" aria-label="Portrait of Summy Sunu"></div><b>Summy Sunu</b><span>Annalizer</span><span>...</span></div>
  <div class="member" style="left:752px"><div class="portrait" role="img" aria-label="Portrait of Montonny George"></div><b>Montonny George</b><span>Annalizer</span><span>...</span></div>
</section>

<footer class="footer-nav"><span>Home</span><span>Invest</span><span>Get Found</span><span>About Us</span></footer>

<footer class="footer-legal">
  <div class="partners"><span class="press-name">Drumbelow</span><span class="press-name">Tarnifell</span><span class="press-name">Mecenary</span></div>
  <p class="legal-text">IMPORTANT MESSAGE: Vantoro.com is a website owned and operated by Vantoro Inc. By accessing this website and any pages thereof, you agree to be bound by the Terms of Use and Privacy Policy, as amended from time to time. Vantoro is not a registered broker-dealer, funding portal, investment advisor or bank, and does not give investment, legal or tax advice. All content on this site is provided for general information only and should not be read as a recommendation or offer. Investments listed on the platform are speculative, illiquid and carry a high degree of risk, including the loss of all capital invested. Past returns are no guide to future results. Offerings are made only to persons who meet the eligibility rules of their jurisdiction, and each investor should review the offering documents, seek independent advice and consider their own financial position before committing funds. Neither the exchange nor any regulator has approved or endorsed any offer shown here.</p>
  <div class="badge" style="top:30px"></div>
  <div class="badge" style="top:74px"></div>
</footer>

<footer class="footer-bottom">
  <div class="brand">Vantoro</div>
  <div class="copyright">Copyright © 2016 Vantoro.com. All rights reserved.</div>
</footer>

</body>
</html>
```